Saucy Velvet Impz Business Card

We need business cards designed for our consultants to use and hand out to customers.
We are an Adult party plan company (like Crelvaware but sex toys and lingerie)
We would like bright colours pinks, purples.
The cards need our logo
Space for the reps phone number email address and name.
We need our website on it www.saucyvelvetimps.com.au

```html
<!DOCTYPE html>
<html lang="en">
<head>
<meta charset="utf-8">
<title>Saucy Velvet Impz Business Card</title>
<link href="https://fonts.googleapis.com/css2?family=Open+Sans:wght@400;700&family=Parisienne&display=swap" rel="stylesheet">
<style>
  :root {
    --magenta: #b3126f;
    --magenta-deep: #8f0c57;
    --magenta-bright: #d0168a;
    --pink-soft: #f58bc8;
    --ink: #555555;
    --white: #ffffff;
    --black: #111111;
    --page: #ffffff;
  }
  * { margin: 0; padding: 0; box-sizing: border-box; }
  html, body {
    width: 1200px; height: 659px; overflow: hidden;
    background: var(--page);
    font-family: "Open Sans", Arial, sans-serif;
  }
  .canvas { position: relative; width: 1200px; height: 659px; }

  .card {
    position: absolute;
    width: 480px; height: 274px;
    box-shadow: 4px 6px 12px rgba(0,0,0,0.35);
    overflow: hidden;
  }

  /* Front */
  .card-front { left: 165px; top: 45px; background: var(--magenta); }
  .photo-band {
    position: absolute; left: 0; top: 60px; width: 256px; height: 154px;
    background: linear-gradient(120deg, #3a1a2e 0%, #c76a9a 35%, #e9b9c8 55%, #7a2d56 80%, #241018 100%);
  }
  .contact-edge {
    position: absolute; top: 0; height: 100%; width: 10px; background: var(--pink-soft);
  }
  .contact-edge.left { left: 256px; }
  .contact-edge.right { left: 440px; }
  .contact-panel {
    position: absolute; left: 266px; top: 0; width: 174px; height: 100%;
    background: var(--white);
    text-align: right; padding: 68px 10px 0 0;
  }
  .dark-strip {
    position: absolute; left: 450px; top: 45px; width: 30px; height: 150px;
    background: var(--black);
  }
  .greeting { color: var(--magenta); font-weight: 700; font-size: 21px; line-height: 1.1; white-space: nowrap; }
  .role { color: var(--ink); font-size: 9px; line-height: 1.2; }
  .office {
    position: absolute; right: 10px; bottom: 20px;
    color: var(--ink); font-size: 10px; line-height: 1.3; white-space: nowrap;
  }
  .office-title { color: var(--magenta); font-weight: 700; font-size: 10.5px; }

  /* Back */
  .card-back {
    left: 455px; top: 340px;
    background: radial-gradient(ellipse at 50% 45%, var(--magenta-bright) 0%, var(--magenta) 55%, var(--magenta-deep) 100%);
    color: var(--white); text-align: center;
  }
  .tagline {
    font-family: "Parisienne", cursive;
    font-size: 40px; font-weight: 400; margin-top: 26px; line-height: 1.2;
  }
  .brand {
    position: absolute; left: 0; right: 0; top: 178px;
    display: flex; align-items: center; justify-content: center; gap: 10px;
    font-family: "Open Sans", Arial, sans-serif; font-weight: 700; font-size: 18px;
  }
  .brand-mark { width: 14px; height: 14px; border-radius: 50%; background: var(--white); }
  .website {
    position: absolute; left: 0; right: 0; top: 214px;
    font-size: 12px; font-weight: 400; letter-spacing: 0.3px;
  }
</style>
</head>
<body>
<main class="canvas">
  <section class="card card-front" aria-label="Business card front">
    <div class="photo-band" role="img" aria-label="Photo of two smiling women in pink party outfits"></div>
    <div class="contact-edge left"></div>
    <div class="contact-panel">
      <p class="greeting">Hi my name is</p>
      <p class="role">consultants</p>
      <div class="office">
        <p class="office-title">Head Office</p>
        <p>Saucy Velvet Impz Pty Ltd</p>
        <p>P.O. Box 481</p>
        <p>Larkfield Vic 3199</p>
        <p>Phone: 0400 555 218</p>
        <p>info@saucyvelvetimps.com.au</p>
      </div>
    </div>
    <div class="contact-edge right"></div>
    <div class="dark-strip"></div>
  </section>

  <section class="card card-back" aria-label="Business card back">
    <h2 class="tagline">Planning a Party ?</h2>
    <div class="brand"><span class="brand-mark"></span><span>Saucy Velvet Imp Parties</span></div>
    <p class="website">www.saucyvelvetimps.com.au</p>
  </section>
</main>
</body>
</html>
```